K & D A/C Compressors' Business Card

Hello,

I need someone to create a new business card for my business. The name of my Business is: K & D A/C Compressors. I sell automotive air conditioning parts (a/c parts). I would like the business card to incorporate my logo, and to have an automotive feel to it. It is important that the business card feel like it is coming from an automotive parts business.

I already have a logo, which I will provide.

Thanks.

Project Deadline Extended Reason: I feel like extending the deadline until October 9, 2017, will allow for more time to design the business card. Thank you for your understanding. Added Monday, October 2, 2017

Target Market(s)

Consumers who need automotive a/c parts, and auto mechanics.

Industry/Entity Type

Automotive

Contact Information for Business Card

Business name: K & D A/C Compressors
Business Address: 48207 Southwest 64th Avenue, North Miami Beach, Florida 33847
Telephone: 305-642-1730
Fax: To be provided once I choose your design.
Website: www.kdcoolparts.example
Email: support@kdcoolparts.example
Names: To be provided once I choose your design.

Font styles to use
Sans Serif

Colors

Designer to choose colors to be used in the design.

Requirements
Must have
• The business card must include all of the "Business Card Details" and the logo I have uploaded.

```html
<!DOCTYPE html>
<html lang="en">
<head>
<meta charset="utf-8">
<title>K &amp; D A/C Compressors – Business Card</title>
<link href="https://fonts.googleapis.com/css2?family=Montserrat:wght@400;500;600&family=Questrial&display=swap" rel="stylesheet">
<style>
  :root {
    --backdrop: #d8d8d8;
    --card-white: #ffffff;
    --brand-blue: #0a9be2;
    --brand-blue-soft: #7fc3e4;
    --ink-dark: #333333;
    --ink-grey: #8c8c8c;
    --logo-grey: #9a9a9a;
  }
  html, body {
    margin: 0;
    padding: 0;
    width: 1200px;
    height: 800px;
    overflow: hidden;
    background: var(--backdrop);
  }
  .canvas {
    position: relative;
    width: 1200px;
    height: 800px;
  }
  .card {
    position: absolute;
    top: 272px;
    width: 469px;
    height: 262px;
    background: var(--card-white);
    overflow: hidden;
  }
  .card--front { left: 61px; }
  .card--back { left: 642px; }

  /* Front */
  .stripe-border {
    position: absolute;
    top: 0;
    width: 30px;
    height: 100%;
    background: linear-gradient(180deg, var(--brand-blue) 0%, var(--brand-blue-soft) 50%, var(--brand-blue) 100%);
  }
  .stripe-border--left { left: 0; }
  .stripe-border--right { right: 0; width: 28px; }

  .wordmark {
    position: absolute;
    left: 124px;
    top: 90px;
    font-family: "Montserrat", sans-serif;
    font-weight: 500;
    color: var(--logo-grey);
    line-height: 1;
  }
  .wordmark__name {
    display: block;
    font-size: 34px;
    letter-spacing: 1px;
    padding-left: 72px;
  }
  .wordmark__trade {
    display: block;
    font-size: 19px;
    margin-top: 8px;
    letter-spacing: 0.5px;
  }

  /* Back */
  .back-panel {
    position: absolute;
    top: 0;
    left: 265px;
    width: 204px;
    height: 100%;
    background: var(--brand-blue);
  }
  .back-graphics {
    position: absolute;
    left: 0;
    top: 0;
  }
  .contact-name {
    position: absolute;
    left: 67px;
    top: 56px;
    margin: 0;
    font-family: "Montserrat", sans-serif;
    font-weight: 500;
    font-size: 15px;
    letter-spacing: 0.5px;
    color: var(--ink-dark);
    line-height: 1;
  }
  .contact-name__last { color: var(--ink-grey); }
  .contact-title {
    position: absolute;
    left: 67px;
    top: 74px;
    margin: 0;
    font-family: "Questrial", sans-serif;
    font-size: 11px;
    color: var(--ink-grey);
    line-height: 1;
  }
  .name-rule {
    position: absolute;
    left: 67px;
    top: 88px;
    width: 198px;
    height: 1px;
    background: var(--brand-blue);
  }
  .contact-group {
    position: absolute;
    left: 67px;
    margin: 0;
    font-family: "Questrial", sans-serif;
    font-size: 10.5px;
    color: var(--ink-dark);
    line-height: 14.5px;
    font-style: normal;
  }
  .contact-group--phone { top: 101px; }
  .contact-group--web { top: 136px; }
  .contact-group--address { top: 174px; }
</style>
</head>
<body>
<main class="canvas">
  <section class="card card--front" aria-label="Business card front">
    <div class="stripe-border stripe-border--left" role="img" aria-label="Diagonal blue stripe border"></div>
    <div class="stripe-border stripe-border--right" role="img" aria-label="Diagonal blue stripe border"></div>
    <h1 class="wordmark">
      <span class="wordmark__name">K &amp; D</span>
      <span class="wordmark__trade">A/C Compressors</span>
    </h1>
  </section>

  <section class="card card--back" aria-label="Business card back">
    <div class="back-panel"></div>
    <svg class="back-graphics" width="469" height="262" viewBox="0 0 469 262" aria-hidden="true">
      <polygon points="29,0 56,0 56,48 42.5,58 29,48" fill="var(--brand-blue)"/>
      <polygon points="29,216 42.5,206 56,216 56,262 29,262" fill="var(--brand-blue)"/>
      <rect x="39.5" y="90" width="6" height="116" rx="3" fill="var(--brand-blue)"/>
      <g fill="#fff" stroke="var(--brand-blue)" stroke-width="1.5">
        <circle cx="42.5" cy="114" r="11"/>
        <circle cx="42.5" cy="149" r="11"/>
        <circle cx="42.5" cy="187" r="11"/>
      </g>
      <!-- phone -->
      <rect x="38.5" y="107" width="8" height="14" rx="1.5" fill="none" stroke="var(--brand-blue)" stroke-width="1.3"/>
      <line x1="41" y1="118.5" x2="44" y2="118.5" stroke="var(--brand-blue)" stroke-width="1"/>
      <!-- monitor -->
      <rect x="36" y="143.5" width="13" height="9" rx="1" fill="none" stroke="var(--brand-blue)" stroke-width="1.3"/>
      <line x1="42.5" y1="152.5" x2="42.5" y2="155" stroke="var(--brand-blue)" stroke-width="1.3"/>
      <line x1="39.5" y1="155.5" x2="45.5" y2="155.5" stroke="var(--brand-blue)" stroke-width="1.3"/>
      <!-- home -->
      <polygon points="42.5,180.5 36,186.5 38,186.5 38,193 47,193 47,186.5 49,186.5" fill="var(--brand-blue)"/>
      <rect x="41.3" y="189" width="2.4" height="4" fill="#fff"/>
    </svg>

    <h2 class="contact-name">MARCO <span class="contact-name__last">ALVAREZ</span></h2>
    <p class="contact-title">Business Manager</p>
    <div class="name-rule"></div>

    <p class="contact-group contact-group--phone">305-642-1730<br>Fax Number</p>
    <p class="contact-group contact-group--web">www.kdcoolparts.example<br>support@kdcoolparts.example</p>
    <address class="contact-group contact-group--address">48207 Southwest 64th Avenue,<br>North Miami Beach, Florida 33847</address>
  </section>
</main>
</body>
</html>
```